Business Card for Luxury Hospitality Industry Career Seeker

Need something Simple, Punctual, and Elegant.

Project goal is to update phone number, layout, and wording

I look forward to working with you to create a business card I can give to managers and employers in the Luxury Hospitality industry. I want to advance a career in this industry handing out cards to managers and directors on my way up.
Updates

Updated graphics preferences in brief - would like my name flanked by small Lion, Compass, & Rope and have the Halworth 5 Star logo on the back Added Saturday, January 14, 2017

Updated Brief:-Some wording has been removed-Card Front should be more simple and tidy now-Card Back word choice & flow is improved Added Sunday, January 15, 2017

Target Market(s)

Luxury Hospitality Industry Employers and Managers

Industry/Entity Type

Hospitality

Contact Information for Business Card

(Card Front)
Corbin T. Pellman (flanked by small Lion, Compass & Rope graphic)
Luxury Hospitality
555-317-8846
ridgefellow@mailvessel.example
netroster.example/in/corbin-pellman-vet-civ
My Experience = Our Success

(Card Back)
Graphic of: Halworth 5 Star logo and maybe QTR 5 Diamond Logo too
8 years military supply, logistics, & administrative experience
2 years intensive recruiting, marketing, and sales expertise
Adept problem solving, planning and management skills
5 Star, 5 Daimond, Luxury Hotels & Hospitality Rooms & Revenue

Requirements
Must have
• Name
• Phone Number
• Email Address
• Net Roster Address
• Slogan (My Experience = Our Success)
• Graphic on back: Halworth 5 Star logo
• Qualification Remarks
• Catchy logo
Nice to have
• Background that makes a viewer think Luxury Hospitality Experience and/or World Experience
• Color combinations I've seen & liked are black & yellow, black & white, and blue & white

```html
<!DOCTYPE html>
<html lang="en">
<head>
<meta charset="utf-8">
<title>Corbin T. Pellman — Business Card</title>
<link rel="stylesheet" href="https://fonts.googleapis.com/css2?family=Source+Sans+3:wght@400;600&display=swap">
<style>
  :root {
    --backdrop: #e9e6e3;
    --card-white: #ffffff;
    --card-black: #000000;
    --ink: #111111;
    --ink-light: #ffffff;
    --badge-blue: #2a4fa3;
    --badge-gold: #b08a3c;
  }
  * { margin: 0; padding: 0; box-sizing: border-box; }
  html, body { width: 1200px; height: 900px; overflow: hidden; }
  body {
    background: var(--backdrop);
    font-family: "Source Sans 3", "Myriad Pro", Arial, sans-serif;
    position: relative;
  }
  .card {
    position: absolute;
    background: var(--card-white);
    box-shadow: 0 6px 18px rgba(0,0,0,0.18);
    overflow: hidden;
  }
  /* Front */
  .card-front { left: 78px; top: 34px; width: 588px; height: 364px; }
  .front-top { position: absolute; left: 0; top: 0; width: 100%; height: 174px; }
  .brand-mark {
    position: absolute; left: 44px; top: 70px;
    display: flex; align-items: center; gap: 10px;
    color: var(--ink); font-weight: 600; font-size: 20px;
  }
  .brand-dot { width: 28px; height: 28px; border-radius: 50%; background: var(--ink); }
  .slogan {
    position: absolute; left: 148px; top: 126px;
    font-size: 17.5px; color: var(--ink);
  }
  .front-band {
    position: absolute; left: 0; top: 174px; width: 100%; height: 190px;
    background: var(--card-black); color: var(--ink-light);
    padding: 9px 0 0 32px;
  }
  .name { font-size: 23px; font-weight: 600; letter-spacing: 0.3px; margin-bottom: 8px; line-height: 28px; }
  .title { font-size: 17px; line-height: 22px; }
  .contact-list { list-style: none; margin-top: 3px; }
  .contact-list li {
    display: flex; align-items: center; gap: 10px;
    font-size: 17px; line-height: 25px;
  }
  .contact-list svg { width: 14px; height: 14px; flex: none; }
  /* Back */
  .card-back { left: 388px; top: 505px; width: 567px; height: 352px; }
  .qualifications {
    list-style: none; text-align: center;
    padding-top: 47px; font-size: 16.5px; line-height: 25.5px; color: var(--ink);
  }
  .back-band { position: absolute; left: 0; top: 170px; width: 100%; height: 131px; }
</style>
</head>
<body>

<section class="card card-front">
  <div class="front-top">
    <div class="brand-mark"><span class="brand-dot"></span>Ridgefellow</div>
    <p class="slogan">My Experience = Our Success</p>
  </div>
  <div class="front-band">
    <h1 class="name">Corbin T. Pellman</h1>
    <p class="title">Reservations Agent Halworth<br>5 Star Luxury Hotel</p>
    <ul class="contact-list">
      <li>
        <svg viewBox="0 0 16 16" aria-hidden="true"><path fill="#fff" d="M3.5 1l2.5 3-1.5 2c1 2 3 4 5 5l2-1.5 3 2.5-1.5 2.5C8 15 1 8 1 2.5z"/></svg>
        555-317-8846
      </li>
      <li>
        <svg viewBox="0 0 16 16" aria-hidden="true"><rect x="1" y="3" width="14" height="10" fill="#fff"/><path d="M1 3l7 6 7-6" stroke="#000" stroke-width="1.4" fill="none"/></svg>
        ridgefellow@mailvessel.example
      </li>
      <li>
        <svg viewBox="0 0 16 16" aria-hidden="true"><circle cx="8" cy="8" r="7.5" fill="#fff"/></svg>
        netroster.example/in/corbin-pellman-vet-civ
      </li>
    </ul>
  </div>
</section>

<section class="card card-back">
  <ul class="qualifications">
    <li>- 8 years military supply, logistics, &amp; administrative experience</li>
    <li>- 2 years intensive recruiting, marketing, and sales expertise</li>
    <li>- Adept problem solving, planning and management skills</li>
    <li>- 5 Star, 5 Daimond, Luxury Hotels &amp; Hospitality Rooms &amp; Revenue</li>
  </ul>
  <svg class="back-band" viewBox="0 0 567 131" aria-hidden="true">
    <rect width="567" height="131" fill="var(--card-black)"/>
    <ellipse cx="284" cy="65" rx="146" ry="70" fill="var(--card-white)"/>
    <rect x="210" y="35" width="60" height="60" rx="6" fill="var(--badge-blue)" opacity="0.85"/>
    <circle cx="355" cy="65" r="30" fill="var(--badge-gold)"/>
  </svg>
</section>

</body>
</html>
```